Professional business cards for real estate development company

I need business cards for my new real estate development company. The company, "KORVA" is a real estate development, investment, and advisory firm with a focus on multifamily, office, and mixed-use projects across primary and secondary markets in the Southeast United States.

Style preference is modern

Industry/Entity Type

Real Estate Development

Contact Information for Business Card

The business cards need to include:
Name
Title
Mailing Address
Phone Number
Web Address

Logo is attached. I would like white to be the primary color with incorporation of the company colors: #232D3A and #B5A451

Font styles to use
Other font styles liked:
• Montserrat, Avenir

Requirements
Must have
• Company Logo. No need to include the company name since the name is in the logo.
Should not have
• No line type designs

```html
<!DOCTYPE html>
<html lang="en">
<head>
<meta charset="UTF-8">
<title>KORVA Development – Business Cards</title>
<link href="https://fonts.googleapis.com/css2?family=Josefin+Sans:wght@300;400;600&display=swap" rel="stylesheet">
<style>
  :root {
    --navy: #232D3A;
    --navy-deep: #1c2430;
    --gold: #B5A451;
    --paper: #fbfbfa;
    --backdrop: #e6e6e4;
    --ink-soft: #3a4350;
  }
  * { box-sizing: border-box; margin: 0; padding: 0; }
  html, body { width: 1200px; height: 801px; overflow: hidden; }
  body {
    background: var(--backdrop);
    font-family: "Josefin Sans", "Montserrat", sans-serif;
    position: relative;
  }
  .card {
    position: absolute;
    top: 252px;
    width: 520px;
    height: 297px;
    border-radius: 3px;
    overflow: hidden;
  }
  .card--front { left: 50px; background: var(--paper); color: var(--navy); }
  .card--back { left: 630px; background: var(--navy); }

  .wordmark {
    position: absolute;
    display: flex;
    align-items: center;
    gap: 12px;
  }
  .wordmark__square {
    width: 22px; height: 22px;
    background: currentColor;
  }
  .wordmark__name {
    font-weight: 600;
    line-height: 1;
    letter-spacing: 2px;
  }
  .wordmark__name span { display: block; font-size: 0.3em; letter-spacing: 0.5em; margin-top: 8px; }

  .card--front .wordmark { left: 40px; top: 112px; color: var(--navy); }
  .card--front .wordmark__name { font-size: 46px; }

  .details {
    position: absolute;
    left: 268px;
    top: 38px;
    width: 222px;
  }
  .rule { height: 2px; background: var(--gold); }
  .details__name {
    margin-top: 30px;
    font-size: 19px;
    font-weight: 400;
    letter-spacing: 1.5px;
    text-transform: uppercase;
  }
  .details__title {
    margin-top: 5px;
    font-size: 11px;
    color: var(--gold);
    margin-bottom: 14px;
    font-weight: 300;
  }
  .details__address {
    margin-top: 18px;
    font-size: 12px;
    font-weight: 300;
    line-height: 1.45;
    color: var(--ink-soft);
  }
  .contacts { list-style: none; margin-top: 14px; }
  .contacts li {
    display: flex; align-items: center; gap: 8px;
    font-size: 12px; font-weight: 300; color: var(--ink-soft);
    margin-bottom: 5px;
  }
  .contacts svg { width: 14px; height: 14px; flex: none; }

  .back__photo {
    position: absolute; inset: 0;
    background: linear-gradient(135deg, #2a3442 0%, #232D3A 45%, #303a48 70%, #1f2833 100%);
  }
  .card--back .wordmark {
    left: 50%; top: 50%;
    transform: translate(-50%, -50%);
    color: #f4f4f2;
  }
  .card--back .wordmark__name { font-size: 56px; }
</style>
</head>
<body>

<section class="card card--front">
  <div class="wordmark">
    <div class="wordmark__square"></div>
    <div class="wordmark__name">KORVA<span>DEVELOPMENT</span></div>
  </div>

  <div class="details">
    <div class="rule"></div>
    <h1 class="details__name">Daniel Reeve</h1>
    <p class="details__title">Partner</p>
    <div class="rule"></div>
    <p class="details__address">2140 Linden Row NE<br>Atlanta, Georgia 30309</p>
    <ul class="contacts">
      <li>
        <svg viewBox="0 0 14 14" aria-hidden="true"><circle cx="7" cy="7" r="7" fill="#B5A451"/><path d="M4.3 3.8l1.4-.3.8 1.8-.9.7a5 5 0 0 0 2.4 2.4l.7-.9 1.8.8-.3 1.4c-3.4.3-6.2-2.5-5.9-5.9z" fill="#fff"/></svg>
        000 0000 00 00
      </li>
      <li>
        <svg viewBox="0 0 14 14" aria-hidden="true"><circle cx="7" cy="7" r="7" fill="#B5A451"/><rect x="3.6" y="4.6" width="6.8" height="4.8" fill="none" stroke="#fff" stroke-width="0.9"/><path d="M3.6 4.6L7 7.4l3.4-2.8" fill="none" stroke="#fff" stroke-width="0.9"/></svg>
        info@korvadevelopment.com
      </li>
      <li>
        <svg viewBox="0 0 14 14" aria-hidden="true"><circle cx="7" cy="7" r="7" fill="#B5A451"/><circle cx="7" cy="7" r="3.4" fill="none" stroke="#fff" stroke-width="0.9"/><path d="M3.6 7h6.8M7 3.6c-1.6 2-1.6 4.8 0 6.8M7 3.6c1.6 2 1.6 4.8 0 6.8" fill="none" stroke="#fff" stroke-width="0.7"/></svg>
        www.korvadevelopment.com
      </li>
    </ul>
  </div>
</section>

<section class="card card--back">
  <div class="back__photo" role="img" aria-label="Dark navy-toned photograph of glass office towers seen from below"></div>
  <div class="wordmark">
    <div class="wordmark__square"></div>
    <div class="wordmark__name">KORVA<span>DEVELOPMENT</span></div>
  </div>
</section>

</body>
</html>
```